Business Cards for an 'affordable luxury' inner city home builder in Calgary.

We need a business card design that emulates the progressive, innovative, culture of our company and the modern style of our homes. Use our website www.velmarcrest-ab.com as a reference for the product we build.

Our company builds homes in the inner city space of Calgary, Alberta. We build affordable luxury.

Target Market(s)

Young professional Families

Contact Information for Business Card

Try to maintain consistency with the logo font and the card font.

Requirements
Must have
• The details must include: Name, education, title, phone number, website and email (Address is not as important)
• The design must be uniques (like our logo), elegant, sophisticated and modern.

```html
<!DOCTYPE html>
<html lang="en">
<head>
<meta charset="utf-8">
<title>Velmarcrest Custom Homes — Business Card</title>
<link rel="stylesheet" href="https://fonts.googleapis.com/css2?family=Questrial&family=Tinos&family=Open+Sans:wght@400&display=swap">
<style>
  :root {
    --page: #e9e8ee;
    --card-back: #b6b3cb;
    --card-front: #a9a7c1;
    --frame: #4d4d52;
    --frame-shine: #c9c9cf;
    --ink: #1d1d20;
    --rule: #55555b;
    --disc: #f1f1f1;
  }
  * { box-sizing: border-box; margin: 0; padding: 0; }
  html, body { width: 1200px; height: 900px; overflow: hidden; }
  body {
    background: var(--page);
    position: relative;
    font-family: "Open Sans", sans-serif;
    color: var(--ink);
  }
  .card {
    position: absolute;
    left: 320px;
    width: 560px;
    height: 320px;
    border-radius: 4px;
    overflow: hidden;
    box-shadow: 0 6px 18px rgba(40, 40, 60, 0.18);
  }
  .card--back { top: 95px; background: var(--card-back); }
  .card--front { top: 485px; background: var(--card-front); }
  .card__frame {
    position: absolute;
    inset: 12px;
    border: 5px solid var(--frame);
    border-radius: 8px;
    box-shadow: inset 0 0 0 1px var(--frame-shine);
    z-index: 2;
  }
  .card__disc {
    position: absolute;
    inset: 0;
    width: 100%;
    height: 100%;
    z-index: 1;
  }

  /* back side */
  .details {
    position: absolute;
    left: 70px;
    top: 118px;
    z-index: 3;
    font-family: "Tinos", serif;
    font-size: 21px;
    line-height: 25px;
  }
  .details__row { display: flex; align-items: flex-end; }
  .details__label { width: 118px; }
  .details__line {
    display: block;
    width: 290px;
    height: 1px;
    background: var(--rule);
    margin-bottom: 6px;
  }
  .details__row:first-child .details__label { width: 70px; }
  .details__row:first-child .details__line { width: 338px; }
  .web-small {
    position: absolute;
    right: 34px;
    bottom: 28px;
    z-index: 3;
    font-family: "Tinos", serif;
    font-size: 11px;
  }
  .web-small span { margin-right: 10px; }

  /* front side */
  .brand {
    position: absolute;
    left: 40px;
    top: 38px;
    z-index: 3;
    display: flex;
    align-items: flex-start;
    gap: 14px;
  }
  .brand__square {
    width: 22px;
    height: 22px;
    background: var(--frame);
    margin-top: 4px;
  }
  .brand__name {
    font-family: "Questrial", sans-serif;
    font-size: 22px;
    line-height: 23px;
    letter-spacing: 1.5px;
    color: var(--ink);
  }
  .web-large {
    position: absolute;
    right: 40px;
    top: 46px;
    z-index: 3;
    font-family: "Tinos", serif;
    font-size: 16px;
  }
  .web-large span { margin-right: 16px; }
  .contact {
    position: absolute;
    left: 44px;
    bottom: 36px;
    z-index: 3;
    font-size: 20px;
    line-height: 20px;
  }
  .contact__item + .contact__item { margin-top: 22px; }
</style>
</head>
<body>

  <section class="card card--back" aria-label="Card back">
    <div class="card__frame"></div>
    <div class="details">
      <div class="details__row"><span class="details__label">Name:</span><span class="details__line"></span></div>
      <div class="details__row"><span class="details__label">Education:</span><span class="details__line"></span></div>
      <div class="details__row"><span class="details__label">Cell:</span><span class="details__line"></span></div>
      <div class="details__row"><span class="details__label">email</span><span class="details__line"></span></div>
    </div>
    <p class="web-small"><span>WEB:</span>www.velmarcrest-ab.com</p>
  </section>

  <section class="card card--front" aria-label="Card front">
    <svg class="card__disc" viewBox="0 0 560 320" preserveAspectRatio="none" aria-hidden="true">
      <circle cx="505" cy="195" r="170" fill="var(--disc)"/>
    </svg>
    <div class="card__frame"></div>
    <div class="brand">
      <span class="brand__square"></span>
      <p class="brand__name">VELMARCREST<br>CUSTOM<br>HOMES LTD</p>
    </div>
    <p class="web-large"><span>WEB:</span>www.velmarcrest-ab.com</p>
    <div class="contact">
      <p class="contact__item">Tel: 403-555-0142</p>
      <p class="contact__item">Email: projects@velmarcrest-ab.com</p>
    </div>
  </section>

</body>
</html>
```